Best in class cloud software provider for retailers needs a new business card design to reflect prod

We are a software company based out of Chicago selling into retailers. We have a new website and marketing collateral that support our new product designs. We are obsessed with simplicity, ease of use, and having a really powerful product set. We have two products as noted on our website - www.brolvane.com - one is a retail task management product and the other is a Help Ticketing product.

At Brolvane we are passionate about creating the best Retail Task Management system in the industry. We bring more than 20 years of retail operations, Workforce Management and Retail Task experience and have a set of web and mobile software features that no one else has. Brolvane enables you to plan and distribute work throughout your organization and ensure it gets done.

We need a new business card design that reflects our new branding, message and approach.

I've attached a few documents that help support what we are building and how our colors look.

There may be additional future work if this goes well.

Thanks,
Mark

President

Target Market(s)

We sell into retailers and are a software company

Industry/Entity Type

Software

Contact Information for Business Card

The card must have

Name
title
address
tele
email
Brolvane logo (someplace)

So for example

It would have for me

Mark Dorsett
President
48 West Harlow Ave. Suite 310
Chicago, IL 60687
3125550187
mdorsett@brolvane.com

Requirements
Must have
• We need to cards for 5 different people - same design different names etc
Nice to have
• should reflect our colors and product and website - be creative - ease of use, simplicity, and power is what the product is about - but we are very forward Brolvane and hear all the time that our product is gorgeous. The font should be consistent with our website, and marketing one pager included
Should not have
• Strange or unfamiliar colors or fonts...

```html
<!DOCTYPE html>
<html lang="en">
<head>
<meta charset="utf-8">
<title>Brolvane Business Card</title>
<link href="https://fonts.googleapis.com/css2?family=Open+Sans:wght@400;600;700&display=swap" rel="stylesheet">
<style>
  :root {
    --brand-blue: #1d6e9e;
    --brand-blue-light: #2479a8;
    --brand-blue-dark: #1a6592;
    --text-grey: #6f6f6f;
    --bar-grey: #7b7b7b;
    --card-white: #f7f7f7;
    --card-shade: #e9e9e9;
    --backdrop: #3b3b3b;
    --rule: rgba(255,255,255,0.55);
  }
  * { margin: 0; padding: 0; box-sizing: border-box; }
  html, body {
    width: 1200px; height: 965px; overflow: hidden;
    background: var(--backdrop);
    font-family: "Open Sans", Arial, sans-serif;
  }
  .canvas { position: relative; width: 1200px; height: 965px; }

  .card {
    position: absolute; left: 247px; width: 708px; height: 403px;
    overflow: hidden;
    box-shadow: 0 4px 14px rgba(0,0,0,0.45);
  }

  /* Front */
  .card-front {
    top: 60px;
    background: radial-gradient(ellipse at 45% 35%, var(--card-white) 0%, var(--card-shade) 100%);
  }
  .wordmark {
    position: absolute; font-weight: 700; letter-spacing: -1px; line-height: 1;
  }
  .card-front .wordmark {
    left: 40px; top: 38px; font-size: 74px; color: var(--brand-blue);
  }
  .name-tab {
    position: absolute; left: -8px; top: 205px; width: 25px; height: 79px;
    border-radius: 8px; background: var(--brand-blue);
  }
  .person { position: absolute; left: 40px; top: 218px; }
  .person-name { font-size: 22px; font-weight: 700; color: var(--brand-blue); line-height: 1.1; }
  .person-title { font-size: 16px; color: var(--text-grey); line-height: 1.3; }

  .address {
    position: absolute; left: 461px; top: 215px;
    font-size: 16.5px; color: var(--text-grey); line-height: 21px;
  }
  .contact-list {
    position: absolute; left: 461px; top: 276px; list-style: none;
    font-size: 16.5px; color: var(--text-grey); line-height: 20.5px;
  }
  .contact-list li { display: flex; align-items: center; }
  .contact-list svg { width: 17px; height: 15px; margin-right: 12px; flex: none; }

  .card-footer { position: absolute; left: 0; top: 355px; }

  /* Back */
  .card-back {
    top: 504px;
    background: radial-gradient(ellipse at 50% 40%, var(--brand-blue-light) 0%, var(--brand-blue-dark) 100%);
  }
  .card-back .wordmark {
    left: 0; right: 0; top: 172px; text-align: center;
    font-size: 62px; color: #ffffff;
  }
  .back-url {
    position: absolute; left: 0; right: 0; top: 375px;
    display: flex; align-items: center; justify-content: center; gap: 16px;
    color: #e8f1f6; font-size: 16px; letter-spacing: 5px;
  }
  .back-url .rule { height: 1px; width: 215px; }
  .rule-left { background: linear-gradient(to right, transparent, var(--rule)); }
  .rule-right { background: linear-gradient(to left, transparent, var(--rule)); }
</style>
</head>
<body>
<main class="canvas">

  <section class="card card-front" aria-label="Business card front">
    <div class="wordmark">Brolvane</div>

    <div class="name-tab"></div>
    <div class="person">
      <p class="person-name">Mark Dorsett</p>
      <p class="person-title">President</p>
    </div>

    <address class="address" style="font-style:normal">
      48 West Harlow Ave. Suite 310<br>
      Chicago, IL 60687
    </address>

    <ul class="contact-list">
      <li>
        <svg viewBox="0 0 16 16" aria-hidden="true"><path fill="var(--brand-blue)" d="M3.5 1.5l2.3 0 1 3.4-1.6 1.3c.9 1.9 2.3 3.3 4.2 4.2l1.3-1.6 3.4 1v2.3c0 .9-.8 1.6-1.7 1.5C6.9 13 3 9.1 2 3.2c-.1-.9.6-1.7 1.5-1.7z"/></svg>
        312 555 01 87
      </li>
      <li>
        <svg viewBox="0 0 18 14" aria-hidden="true"><rect x="0.5" y="1" width="17" height="12" fill="var(--brand-blue)"/><path d="M1 2l8 6 8-6" fill="none" stroke="#fff" stroke-width="1.4"/></svg>
        mdorsett@brolvane.com
      </li>
      <li>
        <svg viewBox="0 0 16 16" aria-hidden="true"><g fill="none" stroke="var(--brand-blue)" stroke-width="1.2"><circle cx="8" cy="8" r="7"/><ellipse cx="8" cy="8" rx="3" ry="7"/><path d="M1 8h14M2.2 4.5h11.6M2.2 11.5h11.6"/></g></svg>
        www.brolvane.com
      </li>
    </ul>

    <svg class="card-footer" width="708" height="48" viewBox="0 0 708 48" aria-hidden="true">
      <path d="M353 48 V14 Q353 6 361 6 H708 V48 Z" fill="var(--brand-blue)"/>
      <path d="M0 14 H339 Q346 14 346 21.5 Q346 29 339 29 H0 Z" fill="var(--bar-grey)"/>
      <path d="M0 29 H339 Q346 29 346 21.5 Q346 38 339 38 H0 Z" fill="none"/>
    </svg>
  </section>

  <section class="card card-back" aria-label="Business card back">
    <div class="wordmark">Brolvane</div>
    <div class="back-url">
      <span class="rule rule-left"></span>
      <span>www.brolvane.com</span>
      <span class="rule rule-right"></span>
    </div>
  </section>

</main>
</body>
</html>
```